Two Wine Labels, One Red One White

We are looking to create a brand image for our wines. There are two requirements by law that we need, however beyond that, the creativity comes from the designer. Required are:
On The Red Label, Alcohol 14.1White Label Alcohol 12.5, The Size, 750ML
SO One label for the red wine with alcohol at 14.1 in a 750 ML Bottle, and one Label for white with alcohol at 12.5 in a 750 ML bottle.

Hi All:
I have some more clarity to assist in the design work.
The Brand Name of the wine is Valmaren for both the red and the white
The name should appear as Valmaren with the Brackets around phonetical as seen here
[vahl-mah-ren] Both the word and the phonetical spelling should appear.
and can be seen on wordplenk.com The Brand Name text can be black
Label should be very light grey, I am trying to capture a Stone grey or texture from stone, although, NOT Marble.
The Red Label, The word "Red" should be in red
The White Label, The word "White" should be in White, all the original remaining elements remain as originally posted.

I look forward to hearing from you for any additional questions.
Updates

Just added a logo Not really seeing what we are trying to achieve, maybe using the logo in the design may assist

Target Market(s)

Wine Aficionados

Requirements
Must have
• Details described in Project Description above, these are required by law. The Name of the Brand will be posted shortly. For the moment if you take the project, just place red on one label and white on the other.
Nice to have
• These two wines are from California (USA), so the Sierra Nevada Mountains could be an inspiration, to outline of California or coast line, a vineyard (of course), a vine...We are in silicon valley, so there is a map of silicon valley with the Bay and ocean, something from a map could work, or let your creativity flow and not use any of these concepts.
Should not have
• I do not not care for decorative fonts, however all else is open

```html
<!DOCTYPE html>
<html lang="en">
<head>
<meta charset="utf-8">
<title>Valmaren Wine Labels</title>
<link href="https://fonts.googleapis.com/css2?family=Playfair+Display:wght@500&family=Tinos&display=swap" rel="stylesheet">
<style>
  :root {
    --backdrop: #e4e3dd;
    --backdrop-light: #f3f3ef;
    --label-red: #f7f7f5;
    --label-white: #cfcdc6;
    --ink: #1d1d1d;
    --ink-soft: #555555;
    --wine-red: #8b3b35;
    --wine-white: #ffffff;
    --halftone-dark: #3a3a3a;
    --halftone-light: #bdbdbd;
  }
  * { margin: 0; padding: 0; box-sizing: border-box; }
  html, body { width: 801px; height: 1200px; overflow: hidden; }
  body {
    position: relative;
    background: radial-gradient(ellipse at 50% 55%, var(--backdrop-light), var(--backdrop) 75%);
    font-family: "Tinos", "Times New Roman", serif;
    color: var(--ink);
  }
  .label { position: absolute; background: var(--label-red); box-shadow: 0 2px 10px rgba(0,0,0,.08); overflow: hidden; }

  /* Red wine: wrap-around label with neck band */
  .wrap-band { left: 70px; top: 330px; width: 300px; height: 52px; }
  .wrap-band .ridge {
    position: absolute; left: 105px; bottom: 0; width: 90px; height: 26px;
    background: linear-gradient(to top, var(--wine-red), #a9554e);
  }
  .wrap-main { left: 70px; top: 388px; width: 300px; height: 400px; }

  /* White wine: square label in stone grey */
  .square { left: 431px; top: 420px; width: 300px; height: 330px; background: var(--label-white); }

  .glass-art {
    position: absolute; left: 0; top: 26px; width: 82px; height: 230px;
    background: linear-gradient(to right, var(--halftone-dark), var(--halftone-light));
    border-radius: 0 40px 40px 0;
    opacity: .85;
  }
  .square .glass-art { top: 14px; height: 200px; width: 70px; }

  .abv {
    position: absolute; right: 14px; top: 8px;
    font-size: 10px; letter-spacing: .3px;
  }
  .volume {
    position: absolute; left: 6px; top: 270px;
    font-size: 10px; white-space: nowrap;
    writing-mode: vertical-rl; transform: rotate(180deg);
  }
  .square .volume { top: 226px; }

  .lockup { position: absolute; right: 14px; bottom: 26px; text-align: right; }
  .square .lockup { bottom: 24px; }
  .variety {
    display: inline-block;
    font-family: "Playfair Display", "Times New Roman", serif;
    font-weight: 500; color: var(--wine-red);
    font-size: 110px; line-height: .9;
    transform: scaleX(.72); transform-origin: right bottom;
  }
  .square .variety { font-size: 88px; color: var(--wine-white); }
  .brand { display: block; font-size: 22px; letter-spacing: 1px; line-height: 1; }
  .square .brand { font-size: 18px; }
  .phonetic { display: block; font-size: 8px; color: var(--ink-soft); text-align: center; margin-top: 2px; }
</style>
</head>
<body>
  <section class="label wrap-band" aria-label="Red wine label neck band">
    <div class="ridge" role="img" aria-label="Red mountain ridge illustration"></div>
  </section>

  <section class="label wrap-main" aria-label="Red wine front label">
    <div class="glass-art" role="img" aria-label="Halftone wine glass illustration"></div>
    <p class="abv">Alcohol 14.1</p>
    <p class="volume">750 ml</p>
    <div class="lockup">
      <span class="variety">Red</span>
      <span class="brand">VALMAREN</span>
      <span class="phonetic">[vahl-mah-ren]</span>
    </div>
  </section>

  <section class="label square" aria-label="White wine label">
    <div class="glass-art" role="img" aria-label="Halftone wine glass illustration"></div>
    <p class="abv">Alcohol 12.5</p>
    <p class="volume">750 ml</p>
    <div class="lockup">
      <span class="variety">White</span>
      <span class="brand">VALMAREN</span>
      <span class="phonetic">[vahl-mah-ren]</span>
    </div>
  </section>
</body>
</html>
```